Organic skincare label - minimalist, earthy, luxe design needed!

I need a label design for a luxury natural skin care line called "Velka Botanix". Velka means 'earth' in Swahili. I would like the design to embody an earthy feel but be minimalistic and give a luxe vibe. My first product will be a Tumeric and Neem Scrub.

The size of the jar is 8oz, label dimensions should be (1.625" Tall x 8.5" Wide)
I will be making other products too such as; oils + toners so I feel free to do labels for glass bottles and/or spray bottles as well.

Forest green, light pinks/nudes/beige, grey, white, gold, are colors that can be used (not all have to be used).

I have included pictures of some things I've worked on myself as well as my original logo design but I need to simplify the logo, no circle around it.
Feel free to get creative.

Thank you! :)
Updates

Target Market(s)

Socially Conscious, Beauty Enthusiast, Minimalist

Industry/Entity Type

Skin Care

Font styles to use
Sans Serif
Other font styles liked:
• "Wonderlove doodle" is the font used for "Velka" in the logo. Feel free to use that or change it as you see fit.

Requirements
Must have
• Simplistic design
would like to stick to a font close to the ones in the logo. Either the one used for the name "Velka" OR the one that the slogan "Pure Plant Care" uses.

I have also included some pictures to capture the aesthetic of my social media and website.

Gender neutral

```html
<!DOCTYPE html>
<html lang="en">
<head>
<meta charset="UTF-8">
<title>Velka Botanix – Tumeric &amp; Neem Scrub Label</title>
<link rel="stylesheet" href="https://fonts.googleapis.com/css2?family=Montserrat:wght@500;600&display=swap">
<style>
  :root {
    --canvas-bg: #e7e7e7;
    --label-bg: #eef0f2;
    --label-vein: #dfe1e3;
    --gold: #d98a2b;
    --ink: #111111;
    --blossom-deep: #c98f9a;
    --blossom-soft: #f1dde0;
  }
  * { margin: 0; padding: 0; box-sizing: border-box; }
  html, body {
    width: 1200px;
    height: 960px;
    overflow: hidden;
    background: var(--canvas-bg);
    font-family: "Montserrat", sans-serif;
  }
  .label {
    position: absolute;
    left: 90px;
    top: 175px;
    width: 1020px;
    height: 611px;
    background:
      linear-gradient(125deg, transparent 40%, var(--label-vein) 48%, transparent 56%),
      linear-gradient(160deg, #f4f5f6 0%, var(--label-bg) 60%, #e9ebed 100%);
    border: 3px solid var(--gold);
    overflow: hidden;
  }
  .blossom-left {
    position: absolute;
    left: 0;
    top: 0;
    width: 186px;
    height: 100%;
    background: radial-gradient(ellipse at 40% 15%, var(--blossom-deep) 0%, var(--blossom-soft) 45%, transparent 75%),
                linear-gradient(180deg, transparent 40%, rgba(201,143,154,0.35) 100%);
  }
  .blossom-right {
    position: absolute;
    right: 0;
    bottom: 0;
    width: 330px;
    height: 442px;
    background: radial-gradient(ellipse at 55% 55%, var(--blossom-soft) 0%, rgba(201,143,154,0.55) 45%, transparent 75%);
  }
  .brand {
    position: absolute;
    left: 0;
    right: 0;
    top: 172px;
    text-align: center;
    color: var(--gold);
  }
  .brand-name {
    font-size: 44px;
    font-weight: 600;
    letter-spacing: 0.5px;
    line-height: 1;
  }
  .brand-slogan {
    margin-top: 16px;
    font-size: 14px;
    font-weight: 600;
    letter-spacing: 0.5px;
  }
  .product-box {
    position: absolute;
    left: 219px;
    top: 283px;
    width: 581px;
    height: 228px;
    border: 2px solid var(--gold);
    display: flex;
    flex-direction: column;
    justify-content: center;
    align-items: center;
  }
  .product-name {
    color: var(--ink);
    font-size: 72px;
    font-weight: 500;
    line-height: 1.2;
    text-align: center;
  }
  .product-name .amp { font-size: 44px; }
  .net-weight {
    position: absolute;
    left: 0;
    right: 0;
    bottom: 6px;
    text-align: center;
    font-size: 28px;
    font-weight: 500;
    color: var(--ink);
  }
</style>
</head>
<body>
  <div class="label">
    <div class="blossom-left" role="img" aria-label="Pink blossom branch illustration"></div>
    <div class="blossom-right" role="img" aria-label="Pale pink cherry blossom flowers illustration"></div>
    <div class="brand">
      <div class="brand-name">Velka Botanix</div>
      <div class="brand-slogan">PURE PLANT CARE</div>
    </div>
    <div class="product-box">
      <div class="product-name">TUMERIC <span class="amp">&amp;</span><br>NEEM SCRUB</div>
    </div>
    <div class="net-weight">8 oz</div>
  </div>
</body>
</html>
```